Verdane Metrics Systems Pte Ltd
Verdane Metrics Systems
Professional
Koren
Tabeli
No. 41, larchmoor Industrial Park E3, #05-22C
Singapore 648213
koren@vms-example.com.sg
www.vms-example.com.sg
209873561K
Business Card and Stationaries Design

```html
<!DOCTYPE html>
<html lang="en">
<head>
<meta charset="utf-8">
<title>Verdane Metrics Systems – Business Cards</title>
<link href="https://fonts.googleapis.com/css2?family=PT+Sans:wght@400;700&display=swap" rel="stylesheet">
<style>
  :root{
    --bg:#e9e6e1;
    --card:#ffffff;
    --blue:#3a7bc8;
    --blue-dark:#2d64a8;
    --orange:#f0791d;
    --ink:#3a3a3a;
    --muted:#6a6a6a;
  }
  *{margin:0;padding:0;box-sizing:border-box}
  html,body{width:1200px;height:852px;overflow:hidden}
  body{background:var(--bg);font-family:"PT Sans",Arial,sans-serif;color:var(--ink);position:relative}

  .card{position:absolute;width:520px;height:300px;background:var(--card);border-radius:18px;overflow:hidden;box-shadow:0 6px 18px rgba(0,0,0,.18)}
  .card--centered{left:70px;top:110px}
  .card--split{left:610px;top:440px}

  .brand{display:flex;align-items:center;gap:10px}
  .brand__mark{width:26px;height:26px;border-radius:50%;background:var(--blue)}
  .brand__name{font-weight:700;font-size:22px;color:var(--blue);line-height:1.05}

  .card__wave{position:absolute;left:0;bottom:0;width:100%;height:110px}

  /* Centered card */
  .card--centered .brand{position:absolute;left:0;right:0;top:42px;justify-content:center}
  .card--centered .person{position:absolute;left:0;right:0;top:118px;text-align:center;font-weight:700;font-size:24px}
  .person__first{color:var(--blue-dark)}
  .person__sep{color:var(--blue-dark);margin:0 4px}
  .person__last{color:var(--orange)}
  .card--centered .license{position:absolute;left:0;right:0;top:156px;text-align:center;font-size:13px;color:var(--muted)}
  .card--centered .address{position:absolute;left:0;right:0;top:182px;text-align:center;font-size:14px}
  .card--centered .links{position:absolute;left:0;right:0;top:204px;display:flex;justify-content:center;gap:18px;font-size:13px}

  .link{display:flex;align-items:center;gap:5px}
  .link__icon{width:12px;height:12px;flex:none}

  /* Split card */
  .card--split .brand{position:absolute;left:36px;top:48px}
  .card--split .person{position:absolute;left:150px;top:124px;text-align:right;font-weight:700;line-height:1.15}
  .card--split .person__first{display:block;font-size:20px}
  .card--split .person__last{display:block;font-size:17px}
  .card--split .details{position:absolute;left:250px;top:122px;font-size:13px;line-height:1.45}
  .card--split .details .link{margin-top:2px}
  .card--split .license{position:absolute;left:40px;top:210px;font-size:12px;color:var(--muted)}
</style>
</head>
<body>

<article class="card card--centered">
  <div class="brand">
    <span class="brand__mark"></span>
    <span class="brand__name">Verdane Metrics Systems</span>
  </div>
  <p class="person"><span class="person__first">Koren</span><span class="person__sep">/</span><span class="person__last">Tabeli</span></p>
  <p class="license">License No : 209873561K</p>
  <p class="address">No. 41, larchmoor Industrial Park E3, #05-22C, Singapore 648213</p>
  <div class="links">
    <span class="link">
      <svg class="link__icon" viewBox="0 0 12 12"><circle cx="6" cy="6" r="6" fill="var(--blue)"/><circle cx="6" cy="6" r="2.4" fill="none" stroke="#fff" stroke-width="1.3"/></svg>
      koren@vms-example.com.sg
    </span>
    <span class="link">
      <svg class="link__icon" viewBox="0 0 12 12"><circle cx="6" cy="6" r="6" fill="var(--blue)"/><path d="M2 6h8M6 1.5c-2 2.5-2 6.5 0 9M6 1.5c2 2.5 2 6.5 0 9" stroke="#fff" stroke-width=".9" fill="none"/></svg>
      www.vms-example.com.sg
    </span>
  </div>
  <svg class="card__wave" viewBox="0 0 520 110" preserveAspectRatio="none">
    <path d="M0 58 C140 96 300 100 520 32 L520 110 L0 110 Z" fill="var(--orange)"/>
    <path d="M0 70 C150 104 320 106 520 46 L520 110 L0 110 Z" fill="var(--card)"/>
    <path d="M0 78 C160 108 340 108 520 58 L520 110 L0 110 Z" fill="var(--blue)"/>
  </svg>
</article>

<article class="card card--split">
  <div class="brand">
    <span class="brand__mark"></span>
    <span class="brand__name">Verdane Metrics Systems</span>
  </div>
  <p class="person"><span class="person__first">Koren</span><span class="person__last">Tabeli</span></p>
  <div class="details">
    <p>No. 41, larchmoor Industrial Park E3,</p>
    <p>#05-22C&nbsp; Singapore 648213</p>
    <span class="link">
      <svg class="link__icon" viewBox="0 0 12 12"><circle cx="6" cy="6" r="6" fill="var(--blue)"/><circle cx="6" cy="6" r="2.4" fill="none" stroke="#fff" stroke-width="1.3"/></svg>
      koren@vms-example.com.sg
    </span>
    <span class="link">
      <svg class="link__icon" viewBox="0 0 12 12"><circle cx="6" cy="6" r="6" fill="var(--blue)"/><path d="M2 6h8M6 1.5c-2 2.5-2 6.5 0 9M6 1.5c2 2.5 2 6.5 0 9" stroke="#fff" stroke-width=".9" fill="none"/></svg>
      www.vms-example.com.sg
    </span>
  </div>
  <p class="license">License No : 209873561K</p>
  <svg class="card__wave" viewBox="0 0 520 110" preserveAspectRatio="none">
    <path d="M0 92 C180 96 360 70 520 12 L520 110 L0 110 Z" fill="var(--orange)"/>
    <path d="M0 98 C190 100 370 82 520 28 L520 110 L0 110 Z" fill="var(--card)"/>
    <path d="M0 102 C200 104 380 92 520 42 L520 110 L0 110 Z" fill="var(--blue)"/>
  </svg>
</article>

</body>
</html>
```